Company or website name

Bright Easel Studio (www.BrightEaselStudio.example)

Links to the website

We are a custom art framing retail establishment that has expanded to provide printing services, photo album services, ready made and custom made frames & mirrors, and we also have an inventory of vintage collectible movie posters. Brighteaselstudio.example

Briefly describe your contest

Design for large storefront billboard

```html
<!DOCTYPE html>
<html lang="en">
<head>
<meta charset="utf-8">
<title>Bright Easel Studio – Storefront Billboard</title>
<link rel="stylesheet" href="https://fonts.googleapis.com/css2?family=Krona+One&family=Michroma&family=Saira:wght@300;700&display=swap">
<style>
  :root {
    --sky-top: #d4e8f4;
    --sky-bottom: #8e9dcc;
    --wave-yellow: #f6f2a6;
    --wave-pink: #f4b2d0;
    --wave-pink-light: #fbe6f0;
    --banner-red: #b5121b;
    --banner-red-light: #d8222c;
    --banner-red-dark: #8c0c12;
    --tab-green: #8fb03a;
    --white: #ffffff;
    --framing-magenta: #e6007e;
    --printing-olive: #8aab2e;
    --albums-blue: #0b4f9f;
  }
  html, body {
    margin: 0;
    padding: 0;
    overflow: hidden;
    background: #ffffff;
  }
  .billboard {
    position: relative;
    width: 800px;
    height: 1200px;
    overflow: hidden;
  }
  .billboard-art {
    position: absolute;
    inset: 0;
    width: 800px;
    height: 1200px;
  }
  .brand-name {
    font-family: "Krona One", sans-serif;
    font-size: 50px;
    fill: var(--white);
  }
  .brand-url {
    font-family: "Michroma", sans-serif;
    font-size: 28px;
    fill: var(--white);
  }
  .artwork-slot {
    position: absolute;
    box-shadow: 4px 6px 12px rgba(0, 0, 0, 0.25);
  }
  .slot-frame {
    left: 78px; top: 280px; width: 404px; height: 292px;
    border-radius: 14px;
    background: linear-gradient(135deg, #f9fafa 0%, #f6dbe7 60%, #efe6ec 100%);
    transform: rotate(4deg);
  }
  .slot-print {
    left: 360px; top: 530px; width: 360px; height: 350px;
    background: linear-gradient(160deg, #fbfbf2 0%, #eceed8 60%, #f4f4ee 100%);
    transform: rotate(6deg);
  }
  .slot-album {
    left: 110px; top: 760px; width: 370px; height: 350px;
    background: linear-gradient(150deg, #f4f4f6 0%, #e8e8ec 50%, #f6f6f8 100%);
    transform: rotate(-9deg);
  }
  .service {
    position: absolute;
    margin: 0;
    font-family: "Saira", sans-serif;
    font-size: 62px;
    line-height: 1;
    white-space: nowrap;
    letter-spacing: -0.5px;
  }
  .service-light { font-weight: 300; }
  .service-bold { font-weight: 700; }
  .service-framing { left: 42px; top: 398px; color: var(--framing-magenta); }
  .service-printing { left: 338px; top: 666px; color: var(--printing-olive); }
  .service-albums { left: 94px; top: 938px; color: var(--albums-blue); }
</style>
</head>
<body>
<main class="billboard">
  <svg class="billboard-art" viewBox="0 0 800 1200" xmlns="http://www.w3.org/2000/svg">
    <defs>
      <linearGradient id="sky" x1="0" y1="0" x2="0" y2="1">
        <stop offset="0" stop-color="var(--sky-top)"/>
        <stop offset="0.3" stop-color="var(--sky-top)"/>
        <stop offset="0.55" stop-color="var(--sky-bottom)"/>
      </linearGradient>
      <radialGradient id="pink-glow" cx="0.12" cy="0.2" r="0.9">
        <stop offset="0" stop-color="var(--wave-pink-light)"/>
        <stop offset="1" stop-color="var(--wave-pink)"/>
      </radialGradient>
      <radialGradient id="banner-glow" cx="0.3" cy="0.1" r="0.8">
        <stop offset="0" stop-color="var(--banner-red-light)"/>
        <stop offset="0.6" stop-color="var(--banner-red)"/>
        <stop offset="1" stop-color="var(--banner-red-dark)"/>
      </radialGradient>
    </defs>

    <rect class="backdrop-sky" width="800" height="1200" fill="url(#sky)"/>
    <path class="backdrop-wave-yellow" d="M0,616 C180,560 420,540 800,580 L800,1200 L0,1200 Z" fill="var(--wave-yellow)"/>
    <path class="backdrop-wave-pink" d="M0,660 C240,570 520,660 800,830 L800,1200 L0,1200 Z" fill="url(#pink-glow)"/>

    <path class="url-tab" d="M50,150 H750 V222 Q750,244 728,244 H72 Q50,244 50,222 Z" fill="var(--tab-green)" stroke="var(--white)" stroke-width="2"/>
    <text class="brand-url" x="400" y="216" text-anchor="middle" textLength="610" lengthAdjust="spacingAndGlyphs">www.BrightEaselStudio.example</text>
    <path class="name-banner" d="M0,0 H800 V140 Q800,162 778,162 H22 Q0,162 0,140 Z" fill="url(#banner-glow)" stroke="var(--white)" stroke-width="2"/>
    <text class="brand-name" x="400" y="122" text-anchor="middle" textLength="716" lengthAdjust="spacingAndGlyphs">Bright Easel Studio</text>
  </svg>

  <div class="artwork-slot slot-frame" role="img" aria-label="Illustration of an empty white picture frame with a pink mat"></div>
  <div class="artwork-slot slot-print" role="img" aria-label="Illustration of a blank printed photo with a white border"></div>
  <div class="artwork-slot slot-album" role="img" aria-label="Illustration of an open photo album page with empty photo slots"></div>

  <h2 class="service service-framing"><span class="service-light">Custom</span> <span class="service-bold">Framing</span></h2>
  <h2 class="service service-printing"><span class="service-light">Image</span> <span class="service-bold">Printing</span></h2>
  <h2 class="service service-albums"><span class="service-light">Photo</span> <span class="service-bold">Albums</span></h2>
</main>
</body>
</html>
```